Kenwick Falcons FC Website

We are looking to develop a new website for Kenwick FC. Kenwick FC has now joined with Kenwick Falcons FC and we are looking at a website that can work for both clubs. Kenwick FC play in a local park football competition while kenwick Falcons are a Semi Professional team that plays in the Coastal Premier Division Competition. What we are after is two separate website off the one platform. I have attached both team logos for you to visualise. Also you can look at the existing kenwick website www.kenwickfc-demo.com.au. We are looking for a huge improvement in the website and it will be imperative we have links to sponsors and the sponsors can get regular visuals. Weare looking to move this club forward and have a very professional website that can communicate clearly with the community.

Hi All,

Please remember that the website is to represent two clubs;
1. Kenwick Falcons FC (Competes in Semi Professional League)
2. Kenwick FC (Compete in HBJCA League which is a lower level)

Further to this the Kenwick Falcons FC page will require a player profile page which will show photos of each player and a little bio on each.

Thanks

Reason: Would like to spend more time review existing and new designs

```html
<!DOCTYPE html>
<html lang="en">
<head>
<meta charset="utf-8">
<title>Kenwick Falcons FC — Contact</title>
<link href="https://fonts.googleapis.com/css2?family=Roboto+Condensed:wght@400;700&family=Open+Sans:wght@400;600;700&family=Playfair+Display:ital@1&family=Oswald:wght@400&display=swap" rel="stylesheet">
<style>
:root{
  --red:#e8231f;
  --red-dark:#cc1412;
  --red-active:#c00f0d;
  --ink:#111;
  --text:#222;
  --muted:#555;
  --panel:#efefef;
  --field:#ffffff;
  --field-line:#dddddd;
  --footer-top:#f6f6f6;
  --footer-bottom:#d9dcdd;
  --sky:#2f4a6b;
  --city:#8a5a32;
  --map:#f4f4f4;
  --tw:#2fa9e0;
  --fb:#4c6fb5;
  --rss:#f08a2c;
  --pin:#e0343c;
}
*{box-sizing:border-box;margin:0;padding:0}
html,body{width:722px;height:1200px;overflow:hidden}
body{position:relative;background:var(--panel);font-family:"Open Sans",Arial,sans-serif;color:var(--text)}
.abs{position:absolute}

/* top bar */
.top-bar{left:0;top:0;width:722px;height:30px;background:var(--red-dark);font-family:"Roboto Condensed",Arial,sans-serif;font-weight:700;font-size:9.5px;color:#fff;text-transform:uppercase}
.top-bar span{position:absolute;top:10px}
.top-bar .divider{position:absolute;top:0;width:1px;height:30px;background:rgba(255,255,255,.25)}
.social-top{position:absolute;top:9px;width:13px;height:12px;background:#fff;border-radius:2px}

/* main nav */
.main-nav{left:0;top:30px;width:722px;height:64px;background:var(--red);font-family:"Roboto Condensed",Arial,sans-serif;font-weight:700;font-size:14.5px;color:#fff}
.main-nav a{position:absolute;top:21px;color:#fff;text-decoration:none}
.main-nav .active-bg{position:absolute;left:570px;top:0;width:90px;height:64px;background:var(--red-active)}
.logo-box{left:312px;top:0;width:96px;height:106px;background:#fff;box-shadow:0 1px 4px rgba(0,0,0,.3);display:flex;flex-direction:column;align-items:center;justify-content:center;gap:6px}
.logo-box .dot{width:30px;height:30px;border-radius:50%;background:var(--red)}
.logo-box .name{font-family:"Roboto Condensed",Arial,sans-serif;font-weight:700;font-size:13px;color:var(--red);text-align:center;line-height:1.1}

/* hero */
.hero{left:0;top:94px;width:722px;height:378px;background:linear-gradient(180deg,#3b4d63 0%,#6b5a48 40%,var(--city) 70%,#3a2a22 100%)}
.hero-rule{left:0;top:472px;width:722px;height:3px;background:var(--red)}
.hero-pin{left:328px;top:219px;width:66px;height:66px;border-radius:50%;background:var(--red)}
.hero-band{left:210px;top:280px;width:300px;height:50px;background:rgba(0,0,0,.55);color:#fff;font-family:"Playfair Display",Georgia,serif;font-style:italic;font-size:29px;text-align:center;line-height:50px;letter-spacing:.5px}

/* contact section */
.mail-badge{left:332px;top:495px;width:58px;height:58px;border-radius:50%;background:var(--red)}
.intro-rule{top:583px;height:1px;background:#cfcfcf}
.intro-title{left:0;top:571px;width:722px;text-align:center;font-family:"Playfair Display",Georgia,serif;font-style:italic;font-size:17.5px;color:var(--ink);letter-spacing:.5px}
.intro-title span{background:var(--panel);padding:0 10px}

.contact-ribbon{left:58px;top:642px;width:164px;height:30px}
.contact-ribbon span{position:absolute;left:0;top:0;width:164px;line-height:30px;text-align:center;font-family:"Roboto Condensed",Arial,sans-serif;font-size:20px;color:#fff}

.field{left:62px;width:272px;height:24px;background:var(--field);border:1px solid var(--field-line);font-size:8.5px;color:#333;padding:6px 6px}
.field.strong{font-weight:700}
.field.message{height:95px;padding-top:8px}
.submit{left:289px;top:913px;width:47px;height:24px;background:var(--red);color:#fff;font-size:8.5px;text-align:center;line-height:24px}

.map{left:402px;top:641px;width:268px;height:158px;background:var(--map);border:2px solid #111;border-radius:3px}
.black-bar{left:404px;width:266px;background:#000;color:#fff;font-size:10.5px;padding-left:2px}
.address{left:404px;top:825px;font-size:11px;line-height:16px;color:#111}
.email{left:404px;top:902px;font-size:11px;color:#111}
.get-in-touch{left:404px;top:919px;width:266px;height:34px;background:#000;color:#fff;font-family:"Oswald",Impact,sans-serif;font-size:23px;line-height:34px;padding-left:6px}
.share{top:961px;width:31px;height:31px;box-shadow:4px 4px 0 rgba(0,0,0,.12)}

/* footer */
.footer-rule{left:0;top:1015px;width:722px;height:4px;background:var(--red)}
.footer{left:0;top:1019px;width:722px;height:167px;background:linear-gradient(180deg,var(--footer-top) 0%,#eeeeee 60%,var(--footer-bottom) 100%)}
.footer-icon{top:1044px;width:38px;height:38px;border-radius:50%}
.footer-col h3{position:absolute;font-family:"Roboto Condensed",Arial,sans-serif;font-weight:700;font-size:17.5px;color:var(--ink)}
.footer-col .underline{position:absolute;height:1px;background:#9a9a9a}
.footer-col ul{position:absolute;list-style:none;font-family:"Roboto Condensed",Arial,sans-serif;font-weight:700;font-size:13.5px;color:#555;line-height:18px}
.bottom-bar{left:0;top:1186px;width:722px;height:14px;background:var(--red);color:#fff;font-size:7.5px;line-height:14px;padding-left:90px}
</style>
</head>
<body>

<header>
  <div class="abs top-bar">
    <span style="left:90px">Join us now ▸</span>
    <div class="divider" style="left:176px"></div>
    <span style="left:200px">Get your tickets ▸</span>
    <span style="left:440px">Follow us :</span>
    <div class="social-top" style="left:506px"></div>
    <div class="social-top" style="left:533px"></div>
    <div class="social-top" style="left:556px"></div>
    <div class="social-top" style="left:579px"></div>
    <div class="social-top" style="left:602px"></div>
  </div>
  <nav class="abs main-nav">
    <div class="active-bg"></div>
    <a style="left:28px">Home</a>
    <a style="left:91px">Photo Gallery</a>
    <a style="left:193px">Fixture &amp; Results</a>
    <a style="left:424px">News</a>
    <a style="left:481px">Sponsor Club</a>
    <a style="left:583px">Contact Us</a>
    <svg class="abs" style="left:671px;top:23px" width="17" height="17" viewBox="0 0 17 17"><circle cx="7" cy="7" r="5.2" fill="none" stroke="#fff" stroke-width="2"/><line x1="11" y1="11" x2="15.5" y2="15.5" stroke="#fff" stroke-width="2.4" stroke-linecap="round"/></svg>
  </nav>
  <div class="abs logo-box">
    <div class="dot"></div>
    <div class="name">Kenwick<br>Falcons FC</div>
  </div>
</header>

<section>
  <div class="abs hero" role="img" aria-label="Aerial photograph of a city skyline at dusk with lit streets"></div>
  <div class="abs hero-rule"></div>
  <div class="abs hero-pin">
    <svg width="66" height="66" viewBox="0 0 66 66"><path d="M33 14c-7.2 0-13 5.6-13 12.6C20 36 33 51 33 51s13-15 13-24.4C46 19.6 40.2 14 33 14z" fill="#fff"/><circle cx="33" cy="27" r="5" fill="var(--red)"/></svg>
  </div>
  <div class="abs hero-band">• LET'S CONNECT •</div>
</section>

<main>
  <div class="abs mail-badge">
    <svg width="58" height="58" viewBox="0 0 58 58"><rect x="16" y="19" width="26" height="19" fill="#fff"/><path d="M16 19l13 11 13-11" fill="none" stroke="var(--red)" stroke-width="2"/><path d="M16 38l10-9M42 38l-10-9" stroke="var(--red)" stroke-width="1.5"/></svg>
  </div>
  <div class="abs intro-rule" style="left:0;width:722px"></div>
  <h2 class="abs intro-title"><span>WANT TO SAY HELLO OR FIND OUT MORE?</span></h2>

  <div class="abs contact-ribbon">
    <svg width="164" height="30" viewBox="0 0 164 30"><path d="M0 0h164l-8 15 8 15H0l8-15z" fill="var(--red)"/></svg>
    <span>CONTACT US</span>
  </div>

  <form>
    <div class="abs field strong" style="top:695px">Name</div>
    <div class="abs field" style="top:731px">Email</div>
    <div class="abs field" style="top:767px">Company</div>
    <div class="abs field message" style="top:805px">Your Message</div>
    <div class="abs submit">SUBMIT</div>
  </form>

  <div class="abs map" role="img" aria-label="Illustrated street map showing the club location"></div>
  <div class="abs black-bar" style="top:809px;height:13px;line-height:13px">KENWICK FC</div>
  <address class="abs address" style="font-style:normal">18 Harbour Rd<br>Kenwick WA 6107<br>Perth, Australia</address>
  <div class="abs black-bar" style="top:888px;height:13px;line-height:13px">Phone: 0400 555 218 - Enquiries only after 5pm</div>
  <div class="abs email">Email: kenwickfc@clubmail-demo.com</div>
  <div class="abs get-in-touch">• Get in touch :</div>
  <div class="abs share" style="left:438px;background:var(--tw)"></div>
  <div class="abs share" style="left:492px;background:var(--fb)"></div>
  <div class="abs share" style="left:546px;background:var(--rss)"></div>
  <div class="abs share" style="left:600px;background:var(--pin)"></div>
</main>

<footer>
  <div class="abs footer-rule"></div>
  <div class="abs footer"></div>

  <div class="abs footer-icon" style="left:46px;background:#e2b43a" role="img" aria-label="Trophy icon"></div>
  <div class="footer-col">
    <h3 style="left:90px;top:1052px">HOME</h3>
    <div class="underline" style="left:90px;top:1081px;width:74px"></div>
    <ul style="left:90px;top:1091px"><li>News</li><li>Gallery</li><li>Sponsor</li><li>Contact Us</li></ul>
  </div>

  <div class="abs footer-icon" style="left:197px;background:#333" role="img" aria-label="Football icon"></div>
  <div class="footer-col">
    <h3 style="left:244px;top:1052px">CLUB</h3>
    <div class="underline" style="left:244px;top:1081px;width:72px"></div>
    <ul style="left:244px;top:1091px"><li>History</li><li>Committee</li><li>Awards</li><li>Forms</li></ul>
  </div>

  <div class="abs footer-icon" style="left:344px;background:#6cb33f;border-radius:4px" role="img" aria-label="Football pitch icon"></div>
  <div class="footer-col">
    <h3 style="left:397px;top:1052px">FIXTURES &amp; RESULTS</h3>
    <div class="underline" style="left:397px;top:1081px;width:272px"></div>
    <ul style="left:397px;top:1091px"><li>Premier League</li><li>Premier League</li><li>ResSuper League</li><li>Super League Res</li></ul>
    <ul style="left:588px;top:1091px;text-align:right;width:76px"><li>Under 10 / 2</li><li>Under 10 / 3</li><li>Under 11 / 1</li><li>Under 12 / 3</li></ul>
  </div>

  <div class="abs bottom-bar">© 2012-2013 All Rights Reserved to Kenwick Falcons FC</div>
</footer>

</body>
</html>
```